Brisley Global Sourcing - we are Asian sourcing agents

We are sourcing agents based in the USA and we act as sourcing agents for clients in throughout the world. We focus primarily on custom sewn goods. So basically companies who do not have the in-house expertise to do it themselves, come to us and have us find suitable factories in Asia to do the production. We are middlemen. We find the factories...quote the project...manage the quality control and then deliver the goods directly to our customer's door. We pride ourselves in making the communication very easy and precise.

Current page is www.brisleysourcing.com

I am not happy w/ the overall look. The spacing...the photos, the fonts...the design elements...the pictures. I want a cool, crisp design that conveys professionalism and clearly depicts/explains what we do.

Coding

Coded - Design and coding required

Number of Pages Required

5+ page

Requirements
Must have
• use my logo....I like it...it was designed by someone on this website.
Nice to have
• a video/animation of the entire process would be wonderful. Showing initial contact with our office in the USA...then to my correspondence with my offices in Taiwan and in Hong Kong...and then back and fort w/ the customer.....and then between my people in Hong Kong/Taiwan with the local factories......and then a quote is generated and sent to my client......to samples being made and sent for approval.....to a PO being generated......to final samples being sent.....to the order being shipped and delivered to the clients warehouse. I was thinking of an animation showing arrows and text showing the back and forth communication and explaining how the process flows.

```html
<!DOCTYPE html>
<html lang="en">
<head>
<meta charset="utf-8">
<title>Brisley Global Sourcing</title>
<link rel="stylesheet" href="https://fonts.googleapis.com/css?family=Open+Sans+Condensed:700|Open+Sans:400,600,700&display=swap">
<style>
:root{
  --green:#78a21e;
  --green-text:#6e9a16;
  --ink:#1f1f1f;
  --body:#4a4a4a;
  --muted:#6b6b6b;
  --line:#d9d9d9;
  --footer:#f1f1f1;
  --footer-bottom:#e2e2e2;
  --white:#ffffff;
}
*{margin:0;padding:0;box-sizing:border-box}
html,body{width:1200px;height:2198px;overflow:hidden;background:var(--white)}
body{position:relative;font-family:"Open Sans",Arial,sans-serif;color:var(--body)}
.abs{position:absolute}

/* header */
.brand{left:190px;top:20px;display:flex;align-items:center;gap:12px}
.brand-mark{width:54px;height:54px;border-radius:50%;background:var(--green)}
.brand-name{font-family:"Open Sans Condensed","Arial Narrow",sans-serif;font-weight:700;font-size:30px;line-height:1;color:#1d3d7a;width:190px}
.account{right:190px;top:6px;font-size:12px;color:var(--muted)}
.search{left:835px;top:42px;width:172px;height:33px;display:flex;border:1px solid var(--line)}
.search span{flex:1;font-size:12px;color:#8a8a8a;padding:8px 10px}
.search i{width:36px;background:var(--green);display:flex;align-items:center;justify-content:center}

.nav{left:0;top:101px;width:1200px;height:57px;background:var(--green)}
.nav ul{position:absolute;left:209px;top:20px;display:flex;gap:15px;list-style:none;white-space:nowrap}
.nav li{font-family:"Open Sans Condensed","Arial Narrow",sans-serif;font-weight:700;font-size:13px;line-height:17px;color:var(--white);text-transform:uppercase}
.social{position:absolute;left:881px;top:14px;display:flex;gap:8px}
.social i{width:28px;height:28px;border-radius:50%;background:var(--white);display:block}

/* hero */
.hero{left:0;top:158px;width:1200px;height:332px;background:radial-gradient(ellipse at 52% 70%,#3ea0e0 0%,#1b5f93 18%,#4a4f55 45%,#8d9094 80%,#b3b5b8 100%)}
.hero-band{left:0;top:270px;width:1200px;height:66px;background:rgba(25,25,25,.62);display:flex;align-items:center;justify-content:center}
.hero-band h1{font-family:"Open Sans Condensed","Arial Narrow",sans-serif;font-weight:700;font-size:38px;color:var(--white);letter-spacing:.5px}

/* intro */
.section-title{left:0;width:1200px;text-align:center;font-family:"Open Sans Condensed","Arial Narrow",sans-serif;font-weight:700;font-size:32px;color:var(--ink);text-transform:uppercase}
.copy{left:202px;width:798px;text-align:center;font-size:11.5px;line-height:22px;color:var(--body)}
.value{width:250px;text-align:center}
.value h3{font-family:"Open Sans Condensed","Arial Narrow",sans-serif;font-weight:700;font-size:20px;line-height:22px;color:var(--green-text);text-transform:uppercase;height:46px}
.value p{font-size:11.5px;line-height:15px;margin-top:16px}

/* products */
.product{top:989px;width:191px;height:141px;border:1px solid #b6cd86;padding:5px}
.product div{width:100%;height:100%}
.product-label{top:1143px;width:191px;text-align:center;font-family:"Open Sans Condensed","Arial Narrow",sans-serif;font-weight:700;font-size:20px;color:var(--green-text);text-transform:uppercase}
.btn-outline{left:497px;top:1204px;width:195px;height:40px;border:2px solid #b6cd86;display:flex;align-items:center;justify-content:center;font-family:"Open Sans Condensed","Arial Narrow",sans-serif;font-weight:700;font-size:16px;color:var(--green-text)}

/* outsource band */
.band{left:0;top:1473px;width:1200px;height:347px;background:linear-gradient(90deg,#4a3b33 0%,#6a5648 25%,#3d3631 50%,#6b5a4c 75%,#3f3530 100%)}
.band-shade{left:0;top:1473px;width:1200px;height:347px;background:rgba(20,20,20,.45)}
.band-title{left:0;top:1510px;width:1200px;text-align:center;font-family:"Open Sans Condensed","Arial Narrow",sans-serif;font-weight:700;font-size:25px;color:var(--white);text-transform:uppercase}
.band-sub{left:0;top:1551px;width:1200px;text-align:center;font-size:14.5px;color:#eee}
.contact-card{top:1626px;height:132px;background:rgba(0,0,0,.72);border:1px solid rgba(255,255,255,.12)}
.avatar{position:absolute;left:24px;top:13px;width:105px;height:105px;border-radius:50%;border:3px solid var(--white);background:linear-gradient(160deg,#c9cdd2,#6e7680)}
.btn-ghost{position:absolute;top:38px;width:176px;height:52px;border:2px solid var(--white);display:flex;align-items:center;justify-content:center;font-family:"Open Sans Condensed","Arial Narrow",sans-serif;font-weight:700;font-size:19px;color:var(--white)}

/* footer */
.footer{left:0;top:1820px;width:1200px;height:294px;background:var(--footer)}
.footer h4{position:absolute;top:44px;font-family:"Open Sans Condensed","Arial Narrow",sans-serif;font-weight:700;font-size:23px;color:var(--green-text);text-transform:uppercase;white-space:nowrap}
.footer ul{position:absolute;top:92px;list-style:none;font-size:12.5px;line-height:25.7px;color:#333}
.contact-lines{position:absolute;left:440px;top:92px;font-size:12px;line-height:18px;color:#333}
.contact-row{position:relative;padding-left:24px;margin-bottom:8px}
.contact-row svg{position:absolute;left:0;top:2px}
.bottom{left:0;top:2114px;width:1200px;height:84px;background:var(--footer-bottom);text-align:center;font-size:11.5px;line-height:22px;color:#444;padding-top:28px}
</style>
</head>
<body>

<header>
  <div class="abs brand">
    <span class="brand-mark"></span>
    <span class="brand-name">BRISLEY GLOBAL SOURCING</span>
  </div>
  <div class="abs account">Login / Register</div>
  <div class="abs search">
    <span>Search Here...</span>
    <i><svg width="15" height="15" viewBox="0 0 16 16"><circle cx="6.5" cy="6.5" r="5" fill="none" stroke="#fff" stroke-width="2"/><line x1="10.2" y1="10.2" x2="15" y2="15" stroke="#fff" stroke-width="2"/></svg></i>
  </div>
  <nav class="abs nav">
    <ul>
      <li>Home</li><li>About Us</li><li>Product Categories</li><li>Sourcing &amp; Procurment</li><li>Request Quote</li><li>Clients</li><li>Contact Us</li>
    </ul>
    <div class="social"><i></i><i></i><i></i><i></i></div>
  </nav>
</header>

<section>
  <div class="abs hero" role="img" aria-label="Hand holding a tablet with a glowing global network of connected devices"></div>
  <div class="abs hero-band"><h1>WE ARE PROVIDE GLOBAL SOURCESS</h1></div>
</section>

<section>
  <h2 class="abs section-title" style="top:532px">Brisley Global Sourcing</h2>
  <p class="abs copy" style="top:585px">Lorem ipsum dolor sit amet, consectetur adipiscing elit. Praesent at tincidunt dolor, nec pulvinar elit. Vivamus imperdiet ipsum lacus, eu suscipit lacus maximus sed. Donec a posuere magna. Fusce finibus, elit nec semper convallis, odio magna feugiat nibh, eget feugiat elit nunc eu erat. Vestibulum ante ipsum primis in faucibus orci luctus et ultrices posuere cubilia Curae; Aliquam ac ipsum in mi luctus bibendum ac vitae nibh. Cras malesuada consequat dui, efficitur ultrices lectus aliquam ut. Nulla congue sollicitudin suscipit. Phasellus luctus fringilla diam convallis elementum. Curabitur quis lobortis est. Proin venenatis luctus efficitur. Nam tempor mattis nibh, id hendrerit felis malesuada ac. Aliquam sit amet urna eu nulla eleifend bibendum sed ut est. Mauris tempus sodales nibh, eget scelerisque sem viverra sed.</p>

  <div class="abs value" style="left:196px;top:768px"><h3>Access Emerging<br>Markets</h3><p>Lorem ipsum dolor sit amet, consectetur adipiscing elit. Praesent at tincidunt dolor, nec pulvinar elit. Vivamus imperdiet ipsum lacus, eu suscipit lacus maximus sed.</p></div>
  <div class="abs value" style="left:471px;top:768px"><h3>Realise Value by Sourcing<br>Direct</h3><p>Lorem ipsum dolor sit amet, consectetur adipiscing elit. Praesent at tincidunt dolor, nec pulvinar elit. Vivamus imperdiet ipsum lacus, eu suscipit lacus maximus sed.</p></div>
  <div class="abs value" style="left:754px;top:768px"><h3>Manage Quality and<br>Reliability Risks</h3><p>Lorem ipsum dolor sit amet, consectetur adipiscing elit. Praesent at tincidunt dolor, nec pulvinar elit. Vivamus imperdiet ipsum lacus, eu suscipit lacus maximus sed.</p></div>
</section>

<section>
  <h2 class="abs section-title" style="top:928px">Featured Products</h2>
  <div class="abs product" style="left:189px"><div role="img" aria-label="Row of colourful phone cases" style="background:linear-gradient(90deg,#e8e8e8,#8a3a8e 30%,#d23a3a 55%,#2a2a2a 80%,#e8e8e8)"></div></div>
  <div class="abs product" style="left:398px"><div role="img" aria-label="Assorted sporting goods and balls" style="background:linear-gradient(135deg,#6b4a2c,#2b2b2b 50%,#a46a35)"></div></div>
  <div class="abs product" style="left:609px"><div role="img" aria-label="Set of travel luggage bags" style="background:linear-gradient(90deg,#f2f2f2,#8c2a35 35%,#3a3a3a 65%,#f2f2f2)"></div></div>
  <div class="abs product" style="left:818px"><div role="img" aria-label="Motorcycle under a blue protective cover" style="background:radial-gradient(ellipse at 50% 55%,#2d3f9a 0%,#4d5fbf 35%,#f4f4f4 70%)"></div></div>
  <div class="abs product-label" style="left:189px">Cases</div>
  <div class="abs product-label" style="left:398px">Sporting Goods</div>
  <div class="abs product-label" style="left:609px">Bags</div>
  <div class="abs product-label" style="left:818px">Covers</div>
  <div class="abs btn-outline">VIEW MORE PRODUCTS</div>
</section>

<section>
  <h2 class="abs section-title" style="top:1284px">Don't Go At It Alone!</h2>
  <p class="abs copy" style="top:1335px;line-height:18px">Brisley Global Sourcing has been sourcing custom sewn goods in Asia since 1998. We work with our clients by matching their unique production needs with the best possible China sewing factories. We manage the entire process from start to finish, by first identifying the best factories to quote each job. The next step is negotiating the best (fair) price possible. We complete the process by monitoring the quality of the goods during production, and then managing the ocean logistics, customs clearances and local delivery right to your door. Our services and our total commitment to customer satisfaction help level the playing field by giving our customers access to low cost, high quality China contract sewing.</p>
</section>

<section>
  <div class="abs band" role="img" aria-label="Blurred crowd of business people"></div>
  <div class="abs band-shade"></div>
  <h2 class="abs band-title">Outsource Your Sewing Needs to Trusted Contractors in China</h2>
  <p class="abs band-sub">Please contact us for immediate consultation regarding your outsourcing project.</p>
  <div class="abs contact-card" style="left:191px;width:394px">
    <div class="avatar" role="img" aria-label="Portrait of a sourcing consultant"></div>
    <div class="btn-ghost" style="left:178px">REQUEST QUOTE</div>
  </div>
  <div class="abs contact-card" style="left:618px;width:391px">
    <div class="avatar" role="img" aria-label="Portrait of a sourcing consultant"></div>
    <div class="btn-ghost" style="left:176px">REQUEST QUOTE</div>
  </div>
</section>

<footer>
  <div class="abs footer">
    <h4 style="left:189px">Sourcing Solutions</h4>
    <ul style="left:191px">
      <li>Bags</li><li>Cases</li><li>Covers</li><li>Gloves</li><li>Medical</li><li>Sewn Goods</li><li>Sporting Goods</li>
    </ul>
    <h4 style="left:440px">Contact Us</h4>
    <div class="contact-lines">
      <div class="contact-row">
        <svg width="12" height="16" viewBox="0 0 12 16"><path d="M6 0C2.7 0 0 2.6 0 5.9 0 10 6 16 6 16s6-6 6-10.1C12 2.6 9.3 0 6 0z" fill="#9a9a9a"/><circle cx="6" cy="6" r="2.2" fill="#f1f1f1"/></svg>
        US HEADQUARTERS<br>Brisley Global Sourcing, LLC<br>Twelve Harbor Street<br>Suite B-2<br>Dover, NH 03820
      </div>
      <div class="contact-row">
        <svg width="15" height="15" viewBox="0 0 16 16"><path d="M3.5 1l3 3-1.8 2a9 9 0 0 0 5.3 5.3l2-1.8 3 3-2 2C6.5 14.5 1.5 9.5 1.5 3z" fill="#9a9a9a"/></svg>
        555-014-2280<br>555-014-2291
      </div>
      <div class="contact-row">
        <svg width="15" height="11" viewBox="0 0 16 12"><rect width="16" height="12" fill="#9a9a9a"/><path d="M0 0l8 6 8-6" fill="none" stroke="#f1f1f1" stroke-width="1.4"/></svg>
        info@brisleysourcing.com
      </div>
    </div>
    <h4 style="left:732px">What Do You Need to Know</h4>
    <ul style="left:733px">
      <li>Contract Sewing in China</li><li>What is the Process?</li><li>What the Minimum Order?</li><li>Contract Outsourcing FAQ</li><li>Outsourcing Case Study</li><li>Custom Industrial Sewing in China</li>
    </ul>
  </div>
  <div class="abs bottom">© Copyright 2015, Brisley Global Sourcing, LLC. All rights reserved.</div>
</footer>

</body>
</html>
```